Cards & Invitations

Hi!
We would like you to design 3 amazing cards for us.
1. Wedding invitation.
We would like to have a spring wedding invitation. It has to be A4 folded to A5 format, floral theme, but made in a very classic style. It has to contain light green and blue colors, but you are free to use other colors as well.
Text to be included:
Mr. and Mrs. Delwyn Avercross
Request the honour of your presence
At the marriage of their daughter
Marisse Avercross
to
Owen Ralditch
Saturday, the eighteenth of April
Two thousand and twelve
At three o'clock in the afternoon
Saint Wendel's Church
58 Brindle Street,
South Hampton, New York
Followed by a dinner at
Restaurant Verlane, Osgood Road 347
R.S.V.P. by the ninth of April
2. Christening invitation in Vintage style.
We need an invitation for a christening of Nico Farrowby. We would like it to be in vintage style, in light pink or lilac color and containing the photo of the baby.
It should also have some church symbols, like cross, prayer beads etc (one element is enough, not all together). Format: A5 horisontal (landscape) card. Please, find the photo attached.
Text to be included:
You are invited to
Witness and Celebrate
the Baptism of our daughter
Nico Farrowby
Sunday, September 26th at 1 p.m.
St. Ambrel Church
5821 Lindqvist Row, Parktown
Reception following the ceremony
at the Farrowby home
7302 Harlowe, Pearl Sound
Please reply by September 18th
3. Birthday invitation.
This is an invitation for Nico's 7th birthday party. The theme is racing. It should contain his photo and a race car (cars) or racing competition. No color preferences. It's a square folded card. Please, find attached the photo.
Text on the outside: Nico is turning 7
Text on the inside:
You are invited to join us
for Nico's 7th Birthday Celebration
Saturday, September 18th
We will have the celebration at Blue Juniper,
486 Quillby Road, Federal Way
Please reply by September 7th
to Bram at 175-389-602
Welcome!

```html
<!DOCTYPE html>
<html lang="en">
<head>
<meta charset="utf-8">
<title>Baptism Invitation – Nico Farrowby</title>
<link rel="stylesheet" href="https://fonts.googleapis.com/css2?family=Goudy+Bookletter+1911&family=Playball&display=swap">
<style>
  :root {
    --page-bg: #ffffff;
    --panel-pink: #e8909c;
    --panel-pink-light: #f0aab3;
    --lace-cream: #f7dcc6;
    --lace-shadow: #ecc4ad;
    --photo-warm: #f1c7c4;
    --photo-skin: #e7a9a8;
    --photo-blanket: #f5e6d3;
    --photo-hat: #ec9fb8;
    --ink: #33232a;
    --ink-soft: #6e3f47;
  }
  * { margin: 0; padding: 0; box-sizing: border-box; }
  html, body {
    width: 1200px; height: 849px; overflow: hidden;
    background: var(--page-bg);
  }
  .invitation {
    position: relative;
    width: 1200px; height: 849px;
    overflow: hidden;
    background: var(--panel-pink);
    font-family: "Goudy Bookletter 1911", Georgia, serif;
    color: var(--ink);
  }
  .baby-photo {
    position: absolute; left: 0; top: 0;
    width: 720px; height: 849px;
    background:
      radial-gradient(ellipse 360px 200px at 170px 110px, var(--photo-hat) 0%, transparent 70%),
      radial-gradient(ellipse 340px 300px at 300px 420px, var(--photo-skin) 0%, transparent 75%),
      radial-gradient(ellipse 420px 260px at 120px 760px, var(--photo-blanket) 0%, transparent 80%),
      linear-gradient(160deg, var(--photo-warm), var(--photo-blanket));
  }
  .lace-border {
    position: absolute; left: 704px; top: 0;
    width: 86px; height: 849px;
    background: linear-gradient(90deg, var(--lace-shadow), var(--lace-cream) 30%, var(--lace-cream) 70%, var(--lace-shadow));
  }
  .cross-ornament {
    position: absolute; left: 898px; top: 34px;
    width: 142px; height: 236px;
    background: var(--panel-pink-light);
    border-radius: 8px;
  }
  .details {
    position: absolute; left: 790px; width: 356px;
    text-align: center;
  }
  .line {
    position: absolute; left: 0; width: 100%;
    font-size: 19px; line-height: 24px; white-space: nowrap;
  }
  .child-name {
    position: absolute; left: 0; width: 100%;
    font-family: "Playball", "Brush Script MT", cursive;
    font-size: 54px; line-height: 60px; white-space: nowrap;
    color: var(--ink);
  }
  .divider {
    position: absolute; left: 40px; top: 616px;
    width: 276px; height: 16px;
  }
  .reply { color: var(--ink-soft); }
</style>
</head>
<body>
  <main class="invitation">
    <div class="baby-photo" role="img" aria-label="Photo of the sleeping newborn girl in a pink knitted hat, with cream lace in the lower corner"></div>
    <div class="lace-border" role="img" aria-label="Vertical cream lace trim"></div>
    <div class="cross-ornament" role="img" aria-label="Ornate filigree cross on a pink damask background"></div>

    <section class="details">
      <p class="line" style="top:406px">You are invited to Witness and Celebrate</p>
      <p class="line" style="top:432px">the Baptism of our daughter</p>
      <h1 class="child-name" style="top:458px">Nico Farrowby</h1>
      <p class="line" style="top:520px">Sunday, September 26th at 1 p.m.</p>
      <p class="line" style="top:550px">St. Ambrel Church</p>
      <p class="line" style="top:578px">5821 Lindqvist Row, Parktown</p>

      <svg class="divider" viewBox="0 0 276 16" aria-hidden="true">
        <line x1="0" y1="8" x2="276" y2="8" stroke="var(--lace-cream)" stroke-width="2"/>
        <path d="M138 2 L146 8 L138 14 L130 8 Z" fill="var(--lace-cream)"/>
      </svg>

      <p class="line" style="top:650px">Reception following the Ceremony</p>
      <p class="line" style="top:678px">at the Farrowby home</p>
      <p class="line" style="top:706px">7302 Harlowe, Pearl Sound</p>
      <p class="line reply" style="top:796px">Please reply by September 18th</p>
    </section>
  </main>
</body>
</html>
```